Business Card Design & logo

Residential building renovation and maintenance work.
All carpentry and joinery needs.
Laying solid timber and floating floors.
Kitchen and bathroom makeovers and modifications.
Interior fitouts,
small job specialist. tiling, plastering, painting,

I would like a silver background. With the use of different shades of grey, rustic orange, black and white.
I do not want pictures of hammers, chisels etc. I am looking for a logo to be incorporated into the card.

Industry/Entity Type

Carpentry

Contact Information for Business Card

BTW Renovations and Maintenance
Lionel Pasquet
0471526083
info@btwrefits.com.au
btwrefits.com.au

```html
<!DOCTYPE html>
<html lang="en">
<head>
<meta charset="utf-8">
<title>BTW Renovations and Maintenance – Business Card</title>
<link rel="stylesheet" href="https://fonts.googleapis.com/css2?family=Oswald:wght@400;500;600&display=swap">
<style>
  :root {
    --backdrop: #e4e4e4;
    --silver-light: #f4f4f4;
    --silver-mid: #d6d6d6;
    --silver-dark: #b9b9b9;
    --rust: #c0623a;
    --charcoal: #555555;
    --ink: #3a3a3a;
    --card-black: #222222;
    --card-black-edge: #2c2c2c;
    --white: #f5f5f5;
  }
  * { box-sizing: border-box; margin: 0; padding: 0; }
  html, body {
    width: 1200px;
    height: 871px;
    overflow: hidden;
    background: var(--backdrop);
    font-family: "Oswald", "Arial Narrow", sans-serif;
  }
  .canvas {
    width: 1200px;
    height: 871px;
    display: flex;
    flex-direction: column;
    align-items: center;
    justify-content: center;
    gap: 30px;
  }
  .card {
    width: 700px;
    height: 400px;
    position: relative;
    overflow: hidden;
    box-shadow: 0 6px 18px rgba(0,0,0,0.18);
  }

  /* Front side */
  .card-front {
    background: linear-gradient(135deg, var(--silver-light) 0%, var(--silver-mid) 55%, var(--silver-dark) 100%);
  }
  .card-front .base-band {
    position: absolute;
    left: 0; right: 0; bottom: 0;
    height: 22px;
    background: var(--rust);
  }
  .brand {
    position: absolute;
    color: var(--rust);
    font-weight: 500;
    letter-spacing: 0.04em;
    line-height: 1.1;
    display: flex;
    align-items: center;
    gap: 10px;
  }
  .brand .brand-mark {
    width: 14px; height: 14px;
    background: var(--rust);
    flex: none;
  }
  .card-front .brand {
    left: 48px;
    top: 160px;
    width: 280px;
    font-size: 22px;
  }
  .divider {
    position: absolute;
    left: 352px;
    top: 70px;
    width: 2px;
    height: 200px;
    background: var(--rust);
  }
  .contact {
    position: absolute;
    left: 384px;
    top: 78px;
    color: var(--ink);
  }
  .contact-name {
    font-size: 34px;
    font-weight: 600;
    letter-spacing: 0.03em;
    margin-bottom: 14px;
  }
  .contact-list { list-style: none; }
  .contact-list li {
    display: flex;
    align-items: center;
    gap: 14px;
    font-size: 19px;
    font-weight: 500;
    letter-spacing: 0.03em;
    margin-bottom: 6px;
    color: var(--ink);
  }
  .contact-list svg { width: 20px; height: 20px; flex: none; }

  /* Back side */
  .card-back {
    background: linear-gradient(160deg, var(--card-black-edge) 0%, var(--card-black) 100%);
  }
  .services {
    position: absolute;
    left: 60px;
    top: 46px;
    list-style: none;
    color: var(--white);
  }
  .services li {
    font-size: 20px;
    font-weight: 400;
    letter-spacing: 0.06em;
    line-height: 1.62;
  }
  .card-back .brand {
    right: 46px;
    bottom: 48px;
    font-size: 24px;
  }
</style>
</head>
<body>
<main class="canvas">

  <section class="card card-front" aria-label="Business card front">
    <div class="brand"><span class="brand-mark"></span><span>BTW Renovations and Maintenance</span></div>
    <div class="divider"></div>
    <div class="contact">
      <h1 class="contact-name">Lionel Pasquet</h1>
      <ul class="contact-list">
        <li>
          <svg viewBox="0 0 20 20" aria-hidden="true"><path fill="#c0623a" d="M3 7c0-2 2-3 7-3s7 1 7 3l-3 1-1-2H7L6 8 3 7zm3 2h8l2 6H4l2-6zm4 1.5a2 2 0 100 4 2 2 0 000-4z"/></svg>
          <span>0471526083</span>
        </li>
        <li>
          <svg viewBox="0 0 20 20" aria-hidden="true"><rect x="2" y="5" width="16" height="11" fill="#c0623a"/><path d="M2 5l8 6 8-6" fill="none" stroke="#e8e8e8" stroke-width="1.4"/></svg>
          <span>info@btwrefits.com.au</span>
        </li>
        <li>
          <svg viewBox="0 0 20 20" aria-hidden="true"><g fill="none" stroke="#c0623a" stroke-width="1.6"><circle cx="10" cy="10" r="7.5"/><ellipse cx="10" cy="10" rx="3.2" ry="7.5"/><path d="M2.5 10h15"/></g></svg>
          <span>btwrefits.com.au</span>
        </li>
      </ul>
    </div>
    <div class="base-band"></div>
  </section>

  <section class="card card-back" aria-label="Business card back">
    <ul class="services">
      <li>- All carpentry and joinery</li>
      <li>- Laying solid timber and floating floors</li>
      <li>- Kitchen makeovers and modifications</li>
      <li>- Bathroom makeovers and modifications</li>
      <li>- Interior fitouts</li>
      <li>- Tiling</li>
      <li>- Plastering</li>
      <li>- Painting</li>
    </ul>
    <div class="brand"><span class="brand-mark"></span><span>BTW Renovations and Maintenance</span></div>
  </section>

</main>
</body>
</html>
```